Pause Your Day And Browse- PYDB poster

I am the Vice President of Advocacy for the Coastline Shelfkeepers Guild. I am looking to have a set of posters made for PYDB (Pause Your Day and Browse) October 23. PYDB is a time when all school children in BC are encouraged to Pause Your Day and Browse for 15-20 minutes at some point in their day.

I would like to get a set of 2 digital posters designed (if possible it would be nice to have the option to print to both 11 x 17 and 8.5 x 11 paper). We need a poster that is high school (Grade 8-12) appropriate and one that is elementary (Grade k-7) appropriate. Both posters need to be replicated in French. All posters need to have the KWNU logo on them as well as the Coastline Shelfkeepers Guild Logo.

Here is a link to last year's successful design http://kwnu-example.org/csg/info/advocacy.html
There are two additional samples in the uploaded files section.

Each poster needs to have the following information:

-Pause Your Day and Browse (PYDB)
- The date Monday, October 23, 2017
-the logo for the KWNU (attached)
-the logo for the CSG (attached)- the logos do not have to be large.

Target Market(s)

Children ages 5-12 and 12-17 as well as their teachers

Industry/Entity Type

Teacher

Font styles to use
Sans Serif

Requirements
Must have
• Must have both logos- colours may be changed for either or both
Nice to have
• Clear, Bright lettering. Images of child or children enjoying reading
Should not have
• stereotypes

```html
<!DOCTYPE html>
<html lang="en">
<head>
<meta charset="UTF-8">
<title>Pause Your Day And Browse – PYDB Poster</title>
<link rel="stylesheet" href="https://fonts.googleapis.com/css2?family=Montserrat:wght@400;500;600;700&display=swap">
<style>
  :root {
    --page-bg: #ecebe8;
    --poster-bg: #ffffff;
    --ink: #111111;
    --navy: #1a2150;
    --deep-space: #101633;
    --nebula-violet: #6b4aa8;
    --nebula-pink: #c46fb3;
    --planet-red: #c8402c;
    --planet-orange: #e0643f;
    --guild-blue: #1f5aa8;
    --guild-green: #3c9a3c;
    --date-text: #ffffff;
  }
  * { margin: 0; padding: 0; box-sizing: border-box; }
  html, body {
    width: 1200px;
    height: 1148px;
    overflow: hidden;
    background: var(--page-bg);
    font-family: "Montserrat", sans-serif;
  }
  .poster {
    position: absolute;
    left: 40px;
    top: 174px;
    width: 1120px;
    height: 800px;
    background: var(--poster-bg);
    box-shadow: 0 2px 10px rgba(0,0,0,0.08);
  }
  .partner-marks {
    position: absolute;
    left: 40px;
    top: 40px;
    display: flex;
    flex-direction: column;
    gap: 16px;
  }
  .partner-mark {
    display: flex;
    align-items: center;
    gap: 8px;
    font-weight: 700;
    font-size: 17px;
    color: var(--navy);
    letter-spacing: 0.5px;
  }
  .partner-mark .dot {
    width: 30px;
    height: 30px;
    border-radius: 50%;
    background: var(--guild-blue);
  }
  .partner-mark .square {
    width: 26px;
    height: 26px;
    background: var(--guild-green);
  }
  .space-illustration {
    position: absolute;
    left: 250px;
    top: 30px;
    width: 620px;
    height: 420px;
  }
  .title {
    position: absolute;
    left: 0;
    width: 100%;
    top: 395px;
    text-align: center;
    font-weight: 500;
    font-size: 225px;
    line-height: 1;
    letter-spacing: 6px;
    background: linear-gradient(100deg, var(--deep-space) 0%, var(--navy) 30%, var(--nebula-violet) 60%, var(--nebula-pink) 80%, var(--navy) 100%);
    -webkit-background-clip: text;
    background-clip: text;
    color: transparent;
  }
  .subtitle {
    position: absolute;
    left: 0;
    width: 100%;
    top: 628px;
    text-align: center;
    font-weight: 500;
    font-size: 31px;
    color: var(--navy);
    letter-spacing: 0.5px;
  }
  .date-row {
    position: absolute;
    left: 0;
    width: 100%;
    top: 680px;
    display: flex;
    justify-content: center;
    align-items: center;
    gap: 26px;
  }
  .date-row .rule {
    width: 80px;
    height: 3px;
    background: var(--ink);
  }
  .date {
    background: var(--ink);
    color: var(--date-text);
    font-weight: 600;
    font-size: 24px;
    padding: 5px 14px;
    letter-spacing: 0.5px;
  }
</style>
</head>
<body>
  <main class="poster">
    <div class="partner-marks">
      <div class="partner-mark"><span class="dot"></span>KWNU</div>
      <div class="partner-mark"><span class="square"></span>CSG</div>
    </div>

    <svg class="space-illustration" viewBox="0 0 620 420" role="img"
         aria-label="Illustration: an astronaut in an orange suit floating in starry space below a red planet, holding up a book">
      <defs>
        <linearGradient id="space-fill" x1="0" y1="0" x2="0" y2="1">
          <stop offset="0" stop-color="var(--planet-red)"/>
          <stop offset="0.2" stop-color="var(--planet-orange)"/>
          <stop offset="0.35" stop-color="var(--nebula-pink)"/>
          <stop offset="0.6" stop-color="var(--nebula-violet)"/>
          <stop offset="1" stop-color="var(--deep-space)"/>
        </linearGradient>
      </defs>
      <polygon points="0,0 620,0 310,420" fill="url(#space-fill)"/>
    </svg>

    <h1 class="title">PYDB</h1>
    <p class="subtitle">PAUSE YOUR DAY AND BROWSE</p>
    <div class="date-row">
      <span class="rule"></span>
      <span class="date">OCTOBER 23, 2017</span>
      <span class="rule"></span>
    </div>
  </main>
</body>
</html>
```